High profile consulting company needs a Business Card Design

I need a business card design for a coaching /consulting company. We specialize in changing behaviors. Our services include therapy, workshops, life coaching, etc.

Check out our website to get a feel for our personality. www.tidewellpartners.com

The new logo will be attached to the website soon, I have attached the new logo for your use on the business card.
Updates

I forgot to provide you with the company email under the "must have" section for the business card.  The website is:

 www.tidewellpartners.com

I understand there's some trouble with the logo I uploaded.  I will try that again.  Thank you for your efforts.

Dalia

Thank you for some of your questions.  I prefer a one sided business card, and tend to like the white backgrounds.

I also made 2 small changes to the content.  

add MFT after the name:  Dalia Forsythe, MFT

and the tag line needed more clarity once I saw it.  Please change it to:  Improving performance by strengthening relationships and changing behaviors.

Thank you,
Dalia

Industry/Entity Type

Business

Requirements
Must have
• logo
Phone number: 321-555-0148
email: Dalia@tidewellpartners.com
Dalia Forsythe, MFT
President
Nice to have
• Improving performance by strengthening relationships and changing behaviors.

```html
<!DOCTYPE html>
<html lang="en">
<head>
<meta charset="utf-8">
<title>Tidewell Partners – Business Card</title>
<link rel="stylesheet" href="https://fonts.googleapis.com/css2?family=Crimson+Pro:ital,wght@0,400;0,600;1,400;1,600;1,700&display=swap">
<style>
  :root {
    --backdrop: #2a2a2a;
    --card-white: #ffffff;
    --brand-green: #12735a;
    --text-grey: #4a4a4a;
    --text-soft: #5c5c5c;
    --faint-mark: #eef3f1;
    --band-text: #ffffff;
  }
  * { box-sizing: border-box; margin: 0; padding: 0; }
  html, body {
    width: 1200px;
    height: 900px;
    overflow: hidden;
    background: var(--backdrop);
  }
  .canvas {
    position: relative;
    width: 1200px;
    height: 900px;
  }
  .business-card {
    position: absolute;
    left: 162px;
    top: 200px;
    width: 876px;
    height: 500px;
    background: var(--card-white);
    overflow: hidden;
    box-shadow: 0 8px 24px rgba(0,0,0,0.45);
    font-family: "Crimson Pro", "Palatino Linotype", serif;
  }
  .faint-circle {
    position: absolute;
    right: -40px;
    top: 0;
    width: 420px;
    height: 420px;
  }
  .brand {
    position: absolute;
    left: 58px;
    top: 34px;
    display: flex;
    align-items: center;
    gap: 16px;
  }
  .brand-dot {
    width: 86px;
    height: 86px;
    border-radius: 50%;
    background: var(--brand-green);
  }
  .brand-name {
    color: var(--brand-green);
    font-weight: 600;
    font-size: 44px;
    line-height: 1;
    letter-spacing: 1px;
    text-transform: uppercase;
  }
  .contact {
    position: absolute;
    left: 66px;
    top: 156px;
    color: var(--text-grey);
    font-style: italic;
  }
  .contact-name {
    font-size: 31px;
    font-weight: 700;
    line-height: 1.1;
  }
  .contact-title {
    font-size: 22px;
    line-height: 1.2;
    color: var(--text-soft);
    margin-top: 4px;
  }
  .contact-links {
    margin-top: 16px;
    font-size: 22px;
    line-height: 1.25;
  }
  .contact-phone {
    margin-top: 14px;
    font-size: 22px;
    line-height: 1.2;
    font-style: normal;
  }
  .tagline-band {
    position: absolute;
    left: 0;
    bottom: 0;
    width: 100%;
    height: 128px;
    background: var(--brand-green);
    color: var(--band-text);
    font-style: italic;
    font-weight: 600;
    font-size: 28px;
    line-height: 1.25;
    padding: 24px 0 0 112px;
  }
  .tagline-band .second-line {
    display: block;
    padding-left: 148px;
  }
</style>
</head>
<body>
<main class="canvas">
  <section class="business-card">
    <svg class="faint-circle" viewBox="0 0 420 420" aria-hidden="true">
      <circle cx="210" cy="210" r="196" fill="none" stroke="var(--faint-mark)" stroke-width="22"/>
    </svg>

    <header class="brand">
      <span class="brand-dot" aria-hidden="true"></span>
      <span class="brand-name">Tidewell Partners</span>
    </header>

    <div class="contact">
      <p class="contact-name">Dalia Forsythe, MFT</p>
      <p class="contact-title">President</p>
      <p class="contact-links">
        www.tidewellpartners.com<br>
        Dalia@tidewellpartners.com
      </p>
      <p class="contact-phone"><em>Ph:</em> 321-555-0148</p>
    </div>

    <footer class="tagline-band">
      "Improving performance by strengthening
      <span class="second-line">relationships and changing behaviors"</span>
    </footer>
  </section>
</main>
</body>
</html>
```